Web Design Project

My site is already up - www.brightvale-hub.com but is very basic at this stage.
I need a to make the design look better and lift it a bit.
I have my own ideas about what I want.
The target market for the site is women - mainly professional, corporate women around the world aged between 28-40 yrs or thereabouts.
There are 3 main areas the site will focus on:
1: Blog and Inbox magazine with contributing writers on various topics from food, diet, emotional intelligence, intuition, feminine energy sexual and non, money to name a few.
2. There is an Ebook that is being added to the site later this year taking a deeper look at all of these topics. For now those subscribing get a free summary of the book.
Book called "Quiet Harbour - Your Gentle Map to a Calmer Day"
Happy to use the title for the FREE summary for subscribers.
3. Events / retreats. We are kicking off with our first Brightvale-hub retreat in Bali in late Oct 2012. We have amazing shots of the villa we will use and the activities etc that will make up a part of the retreat.
Yoga & meditation
Surfing
Photography
Keen to see what you all come up with.
NOTE: I dont want anything too busy. Keep it fairly clean, simple and in keeping with the general look and feel right now.
Target Market(s)
Look and feel
Each slider illustrates characteristics of the customer's brand and the style your logo design should communicate.

```html
<!DOCTYPE html>
<html lang="en">
<head>
<meta charset="utf-8">
<title>Brightvale-hub</title>
<link rel="stylesheet" href="https://fonts.googleapis.com/css2?family=Noto+Sans:wght@400;700&family=Arimo:wght@400&display=swap">
<style>
:root{
  --sun:#f8d60a;
  --ink:#555;
  --ink-soft:#999;
  --ink-light:#8a8a8a;
  --rule:#e3edf0;
  --frame:#e5e5e5;
  --panel-top:#ececec;
  --panel-bottom:#f6f6f6;
  --white:#fff;
  --map-edge:#f8c040;
}
*{box-sizing:border-box;margin:0;padding:0}
html,body{width:1200px;height:1102px;overflow:hidden;background:var(--white)}
body{position:relative;font-family:"Noto Sans",sans-serif;color:var(--ink)}
.abs{position:absolute}
.site-header{left:47px;top:6px;width:1106px;height:188px;background:var(--sun)}
.brand{left:29px;top:54px;display:flex;align-items:center;gap:14px}
.brand-dot{width:64px;height:64px;border-radius:50%;background:var(--white)}
.brand-name{font-size:42px;color:var(--white);font-weight:400;letter-spacing:.5px}
.account-link{right:37px;top:30px;font-size:12px;color:#8a7a2a;letter-spacing:.6px}
.main-nav{right:37px;top:152px;display:flex;gap:31px;font-family:"Arimo",sans-serif;font-size:17px;color:var(--white)}
.main-nav .current{color:#8a8a7a}
.top-rule{left:47px;top:229px;width:1106px;height:1px;background:var(--rule)}
.feature{width:259px}
.photo{width:259px;height:194px;background:var(--frame);padding:12px}
.photo div{width:100%;height:100%}
.feature h2{margin-top:46px;font-size:37px;line-height:1.02;font-weight:400;color:var(--ink-soft)}
.feature p{margin-top:20px;font-size:14.5px;letter-spacing:.3px;line-height:29.3px;height:146px;overflow:hidden;color:#666}
.rule{height:1px;background:var(--rule);left:47px;width:847px}
.block h3{font-size:17px;font-weight:400;color:var(--ink-light);letter-spacing:.4px}
.address{margin-top:6px;font-size:12.5px;line-height:22.4px;color:var(--ink-light);letter-spacing:.5px}
.map{left:341px;top:826px;width:236px;height:118px;border:2px solid var(--map-edge);background:linear-gradient(135deg,#ece7dd,#dcd7cc 60%,#e8e3da)}
.newsletter-field{left:47px;top:1046px;width:259px;height:37px;border:1px solid #e6e6e6;display:flex;align-items:center;padding:0 5px 0 10px;justify-content:space-between}
.newsletter-field span{font-size:14px;color:#aaa}
.newsletter-field b{background:#e6e6e6;color:#888;font-size:15px;padding:3px 12px;letter-spacing:.5px}
.small-text{font-size:12.5px;line-height:22.4px;color:var(--ink-light);letter-spacing:.5px;margin-top:12px}
.offer{left:941px;top:265px;width:212px;height:376px;border-radius:13px;background:linear-gradient(160deg,var(--panel-top) 0%,#e2e2e2 45%,var(--panel-bottom) 46%,var(--white) 100%);padding:36px 10px 0}
.offer .lead{font-size:15px;font-weight:700;color:#333;letter-spacing:.5px}
.offer .free{font-size:25px;font-weight:700;color:#333;line-height:1.2;margin-top:2px}
.offer .title{font-size:25px;font-weight:700;color:var(--sun);line-height:1.15;letter-spacing:.3px}
.offer .sub{font-size:15px;text-align:center;line-height:22px;margin-top:8px;color:#444;letter-spacing:.3px}
.field{width:188px;height:24px;border:1px solid #aaa;background:var(--white);font-size:12.5px;color:#666;padding:2px 5px;margin-top:10px}
.field.first{margin-top:33px}
.cta{display:block;margin:15px auto 0;width:106px;height:33px;border-radius:8px;background:var(--sun);color:var(--white);font-size:18px;font-weight:700;text-align:center;line-height:33px;letter-spacing:1px}
.privacy{font-size:10px;text-align:center;margin-top:36px;color:#444;letter-spacing:.8px}
.follow{left:961px;top:678px;font-size:13px;color:var(--ink-soft);letter-spacing:1px}
.social{left:961px;top:706px;display:flex;gap:9px}
.social span{width:35px;height:35px;border-radius:6px;background:#c9d6de}
</style>
</head>
<body>
<header class="site-header abs">
  <div class="brand abs"><span class="brand-dot"></span><span class="brand-name">brightvale-hub.com</span></div>
  <div class="account-link abs">Login or Register</div>
  <nav class="main-nav abs"><span class="current">Home</span><span>About</span><span>Blog</span><span>Community</span><span>Retreats</span><span>Contact</span></nav>
</header>
<div class="top-rule abs"></div>

<article class="feature abs" style="left:47px;top:265px">
  <div class="photo"><div role="img" aria-label="Woman relaxing on grass with arms open" style="background:linear-gradient(160deg,#8fb060,#6a8f45 55%,#8ea9c4)"></div></div>
  <h2>Curabitur in metus</h2>
  <p>Lorem ipsum dolor sit amet, consectetur adipiscing elit. Mauris tincidunt arcu a ipsum congue mattis. Donec iaculis risus ornare lorem bibendum facilisis. Morbi ut</p>
</article>
<article class="feature abs" style="left:341px;top:265px">
  <div class="photo"><div role="img" aria-label="Bundle of fresh rhubarb stalks" style="background:radial-gradient(ellipse at center,#e2606a 0%,#f2a0a6 45%,#fff 75%)"></div></div>
  <h2>Curabitur in metus</h2>
  <p>Lorem ipsum dolor sit amet, consectetur adipiscing elit. Mauris tincidunt arcu a ipsum congue mattis. Donec iaculis risus ornare lorem bibendum facilisis. Morbi ut</p>
</article>
<article class="feature abs" style="left:635px;top:265px">
  <div class="photo"><div role="img" aria-label="Engineer in hard hat at an industrial site" style="background:linear-gradient(180deg,#5f88c4,#8fb0dc 55%,#5a5f66)"></div></div>
  <h2>Curabitur in metus</h2>
  <p>Lorem ipsum dolor sit amet, consectetur adipiscing elit. Mauris tincidunt arcu a ipsum congue mattis. Donec iaculis risus ornare lorem bibendum facilisis. Morbi ut</p>
</article>

<div class="rule abs" style="top:765px"></div>

<section class="block abs" style="left:47px;top:791px">
  <h3>Massa:</h3>
  <div class="address">412 Harbour Lane West<br>Suite 18 Meadow Court Rise<br>Phone: (02) 7431 9026<br>Fax: (02) 7431 9027<br>Email: hello@brightvale-hub.com</div>
</section>
<section class="block abs" style="left:341px;top:791px"><h3>How to find us:</h3></section>
<div class="map abs" role="img" aria-label="Street map showing the office location"></div>
<section class="block abs" style="left:635px;top:791px">
  <h3>Mauris:</h3>
  <div class="address">412 Harbour Lane West<br>Suite 18 Meadow Court Rise<br>Phone: (02) 7431 9026<br>Fax: (02) 7431 9027<br>Email: hello@brightvale-hub.com</div>
</section>

<div class="rule abs" style="top:979px"></div>

<section class="block abs" style="left:47px;top:1006px"><h3>Subscribe to our newsletter</h3></section>
<div class="newsletter-field abs"><span>you@example.com</span><b>Sign up</b></div>
<section class="block abs" style="left:341px;top:1006px">
  <h3>Harbourline HR Services</h3>
  <div class="small-text">Vestibulum ligula justo, ultricies<br>A iaculis at, cursus quis lacus. Proin vitae mauris</div>
</section>

<aside class="offer abs">
  <div class="lead">Sign up &amp; get your</div>
  <div class="free">FREE copy of</div>
  <div class="title">Quiet Harbour</div>
  <div class="sub">Your Gentle Map<br>to a Calmer Day</div>
  <div class="field first">Your name</div>
  <div class="field">Email</div>
  <span class="cta">Sign up</span>
  <div class="privacy">We respect your privacy</div>
</aside>
<div class="follow abs">Follow us</div>
<div class="social abs"><span></span><span></span><span></span><span></span></div>
</body>
</html>
```